Design for an iOS and Android app managing shopping list

The app allows you to keep manage shopping lists, each shopping list being made of items to buy...
We need a design for the 3 screens of the app:
a) global view showing list of (shopping) list
b) form enabling to edit the name of a (shopping) list
c) detailed view listing the contents/items of a (shopping) list
d) 1 text page [not illustrated]
2 "alerts" items are also to be designed: confirm and error pop ups.
No specific guidelines, nor logo or whatever.
It will be a free app distributed on iOS and Androïd.
We just want to make it looking nice & very usable for end users.

```html
<!DOCTYPE html>
<html lang="fr">
<head>
<meta charset="utf-8">
<title>Shopping lists app – screens</title>
<link rel="stylesheet" href="https://fonts.googleapis.com/css2?family=Nunito:wght@400;600;700&display=swap">
<style>
  :root{
    --bg:#ee6b58;
    --bar:#0a4fa6;
    --bar-dark:#083f86;
    --body:#c9d6ee;
    --row:#ffffff;
    --row-line:#aebfdf;
    --ink:#1d2433;
    --ink-soft:#5a6272;
    --green:#1fa653;
    --red:#e2262d;
    --white:#ffffff;
    --veil:rgba(28,33,44,.62);
    --btn-grey:#e4e4e4;
  }
  *{box-sizing:border-box;margin:0;padding:0}
  html,body{width:1200px;height:552px;overflow:hidden}
  body{background:var(--bg);font-family:"Nunito",Arial,sans-serif;color:var(--ink);position:relative}

  .screen{position:absolute;top:134px;width:160px;height:284px;background:var(--body);overflow:hidden;border-radius:2px;box-shadow:0 3px 10px rgba(0,0,0,.12)}
  .screen--lists{left:48px}
  .screen--rename{left:284px}
  .screen--warning{left:520px}
  .screen--items{left:756px}
  .screen--remove{left:992px}

  .status{height:10px;background:var(--bar-dark);color:var(--white);font-size:5px;font-weight:600;display:flex;align-items:center;justify-content:space-between;padding:0 5px}
  .nav{height:22px;background:var(--bar);color:var(--white);display:flex;align-items:center;justify-content:space-between;padding:0 6px;font-size:7.5px;font-weight:700}
  .nav svg{width:9px;height:9px;stroke:var(--white);fill:none;stroke-width:2;stroke-linecap:round}
  .nav .spacer{width:9px}

  .content{padding:8px 7px}

  .btn{display:inline-flex;align-items:center;gap:3px;height:15px;padding:0 6px;font-size:6.5px;font-weight:600;color:var(--white);border-radius:1px}
  .btn svg{width:6px;height:6px;stroke:var(--white);fill:none;stroke-width:2.2;stroke-linecap:round}
  .btn--green{background:var(--green)}
  .btn--blue{background:var(--bar)}
  .btn--red{background:var(--red)}
  .toolbar{display:flex;gap:6px;margin-bottom:8px}
  .toolbar .btn{flex:1;justify-content:center}

  .list{list-style:none;display:flex;flex-direction:column;gap:2px}
  .list-row{height:16px;background:var(--row);border-bottom:1px solid var(--row-line);display:flex;align-items:center;justify-content:space-between;padding:0 5px;font-size:6.5px;font-weight:600}
  .list-row svg{width:7px;height:7px;stroke:var(--ink);fill:none;stroke-width:1.8;stroke-linecap:round;stroke-linejoin:round}

  .field{height:18px;background:var(--white);border:1px solid var(--row-line);display:flex;align-items:center;padding:0 5px;font-size:7px;font-weight:700;margin-top:2px}
  .form-actions{display:flex;justify-content:space-between;padding:0 9px;margin-top:14px}
  .form-actions .btn{width:42px;justify-content:center}

  .item{display:flex;gap:2px;height:15px}
  .check{width:15px;background:var(--row);display:flex;align-items:center;justify-content:center}
  .check svg{width:9px;height:9px;stroke:var(--green);fill:none;stroke-width:2.4;stroke-linecap:round;stroke-linejoin:round}
  .item-name{flex:1;background:var(--row);display:flex;align-items:center;justify-content:space-between;padding:0 5px;font-size:6px;font-weight:600}
  .item-name svg{width:6px;height:6px;stroke:var(--ink);fill:none;stroke-width:2;stroke-linecap:round}
  .items{display:flex;flex-direction:column;gap:2px;margin-top:6px}

  .veil{position:absolute;inset:0;background:var(--veil)}
  .dialog{position:absolute;left:12px;right:12px;background:var(--white);padding:7px 7px 6px;font-size:5.6px;line-height:1.35;box-shadow:0 2px 8px rgba(0,0,0,.3)}
  .dialog h2{font-size:7px;font-weight:700;text-align:center;margin-bottom:3px}
  .dialog-actions{display:flex;justify-content:flex-end;gap:6px;margin-top:6px}
  .dialog-actions .plain{background:var(--btn-grey);padding:3px 5px;font-weight:700;font-size:5.6px}
  .dialog-actions--split{justify-content:space-between}
  .screen--warning .dialog{top:110px}
  .screen--remove .dialog{top:62px}
</style>
</head>
<body>
<svg width="0" height="0" style="position:absolute" aria-hidden="true">
  <defs>
    <symbol id="i-menu" viewBox="0 0 10 10"><path d="M1 2.5h8M1 5h8M1 7.5h8"/></symbol>
    <symbol id="i-plus" viewBox="0 0 10 10"><path d="M5 1v8M1 5h8"/></symbol>
    <symbol id="i-back" viewBox="0 0 10 10"><path d="M9 5H1.5M5 1.5 1.5 5 5 8.5"/></symbol>
    <symbol id="i-next" viewBox="0 0 10 10"><path d="M1 5h7.5M5 1.5 8.5 5 5 8.5"/></symbol>
    <symbol id="i-pen" viewBox="0 0 10 10"><path d="M1.5 8.5 8.5 1.5"/></symbol>
    <symbol id="i-tick" viewBox="0 0 10 10"><path d="M1.5 5.2 4 7.6 8.6 2.4"/></symbol>
    <symbol id="i-cross" viewBox="0 0 10 10"><path d="M2 2l6 6M8 2 2 8"/></symbol>
  </defs>
</svg>

<!-- a) Lists overview -->
<section class="screen screen--lists">
  <div class="status"><span>●●●○○ NOVA</span><span>4:21 PM</span><span>22%</span></div>
  <header class="nav"><svg><use href="#i-menu"/></svg><span>My Lists</span><svg><use href="#i-plus"/></svg></header>
  <div class="content">
    <div class="toolbar">
      <span class="btn btn--green"><svg><use href="#i-plus"/></svg>Add new list</span>
      <span class="btn btn--blue"><svg><use href="#i-pen"/></svg>Edit</span>
    </div>
    <ul class="list">
      <li class="list-row">Diner de ce soir<svg><use href="#i-next"/></svg></li>
      <li class="list-row">Course Noel<svg><use href="#i-next"/></svg></li>
      <li class="list-row">Courses MEUBLO<svg><use href="#i-next"/></svg></li>
      <li class="list-row">Delmarché<svg><use href="#i-next"/></svg></li>
      <li class="list-row">Diner de ce soir<svg><use href="#i-next"/></svg></li>
      <li class="list-row">Course Noel<svg><use href="#i-next"/></svg></li>
      <li class="list-row">Courses MEUBLO<svg><use href="#i-next"/></svg></li>
      <li class="list-row">Delmarché<svg><use href="#i-next"/></svg></li>
    </ul>
  </div>
</section>

<!-- b) Rename form -->
<section class="screen screen--rename">
  <div class="status"><span>●●●○○ NOVA</span><span>4:21 PM</span><span>22%</span></div>
  <header class="nav"><svg><use href="#i-back"/></svg><span>Update list name</span><span class="spacer"></span></header>
  <div class="content">
    <div class="field">Diner de ce soir</div>
    <div class="form-actions">
      <span class="btn btn--green"><svg><use href="#i-tick"/></svg>Save</span>
      <span class="btn btn--red"><svg><use href="#i-cross"/></svg>Cancel</span>
    </div>
  </div>
</section>

<!-- Error alert -->
<section class="screen screen--warning">
  <div class="status"><span>●●●○○ NOVA</span><span>4:21 PM</span><span>22%</span></div>
  <header class="nav"><svg><use href="#i-back"/></svg><span>Update list name</span><svg><use href="#i-plus"/></svg></header>
  <div class="content">
    <div class="field">Diner de ce soir</div>
    <div class="form-actions">
      <span class="btn btn--green"><svg><use href="#i-tick"/></svg>Save</span>
      <span class="btn btn--red"><svg><use href="#i-cross"/></svg>Cancel</span>
    </div>
  </div>
  <div class="veil"></div>
  <div class="dialog" role="alertdialog">
    <h2>Warning</h2>
    <p>List name should have atleast 1 character to be valid</p>
    <div class="dialog-actions"><span class="plain">OK</span></div>
  </div>
</section>

<!-- c) List detail -->
<section class="screen screen--items">
  <div class="status"><span>●●●○○ NOVA</span><span>4:21 PM</span><span>22%</span></div>
  <header class="nav"><svg><use href="#i-back"/></svg><span>My List</span><svg><use href="#i-plus"/></svg></header>
  <div class="content">
    <span class="btn btn--green"><svg><use href="#i-plus"/></svg>Add new item</span>
    <ul class="items">
      <li class="item"><span class="check"><svg><use href="#i-tick"/></svg></span><span class="item-name">serviettes<svg><use href="#i-cross"/></svg></span></li>
      <li class="item"><span class="check"><svg><use href="#i-tick"/></svg></span><span class="item-name">oignons<svg><use href="#i-cross"/></svg></span></li>
      <li class="item"><span class="check"></span><span class="item-name">bougies<svg><use href="#i-cross"/></svg></span></li>
      <li class="item"><span class="check"></span><span class="item-name">airelles<svg><use href="#i-cross"/></svg></span></li>
      <li class="item"><span class="check"><svg><use href="#i-tick"/></svg></span><span class="item-name">foie gras<svg><use href="#i-cross"/></svg></span></li>
      <li class="item"><span class="check"></span><span class="item-name">soumon fume<svg><use href="#i-cross"/></svg></span></li>
      <li class="item"><span class="check"><svg><use href="#i-tick"/></svg></span><span class="item-name">huile d'olive<svg><use href="#i-cross"/></svg></span></li>
      <li class="item"><span class="check"><svg><use href="#i-tick"/></svg></span><span class="item-name">Delmarché<svg><use href="#i-cross"/></svg></span></li>
    </ul>
  </div>
</section>

<!-- Confirm alert -->
<section class="screen screen--remove">
  <div class="status"><span>●●●○○ NOVA</span><span>4:21 PM</span><span>22%</span></div>
  <header class="nav"><svg><use href="#i-menu"/></svg><span>My Lists</span><svg><use href="#i-plus"/></svg></header>
  <div class="content">
    <div class="toolbar">
      <span class="btn btn--green"><svg><use href="#i-plus"/></svg>Add new list</span>
      <span class="btn btn--blue"><svg><use href="#i-pen"/></svg>Edit</span>
    </div>
    <ul class="list">
      <li class="list-row">Diner de ce soir<svg><use href="#i-next"/></svg></li>
      <li class="list-row">Course Noel<svg><use href="#i-next"/></svg></li>
      <li class="list-row">Courses MEUBLO<svg><use href="#i-next"/></svg></li>
      <li class="list-row">Delmarché<svg><use href="#i-next"/></svg></li>
      <li class="list-row">Diner de ce soir<svg><use href="#i-next"/></svg></li>
      <li class="list-row">Course Noel<svg><use href="#i-next"/></svg></li>
      <li class="list-row">Courses MEUBLO<svg><use href="#i-next"/></svg></li>
      <li class="list-row">Delmarché<svg><use href="#i-next"/></svg></li>
    </ul>
  </div>
  <div class="veil"></div>
  <div class="dialog" role="alertdialog">
    <h2>Remove shopping list</h2>
    <p>Would you like to delete the shopping list: “Diner de ce soir”?</p>
    <div class="dialog-actions dialog-actions--split"><span class="plain">CANCEL</span><span class="plain">CONFIRM</span></div>
  </div>
</section>
</body>
</html>
```